dorwial business card design so that it looks better

need a new business card designed. use our website, dorwian.com for example. I attached an example of a previous card we had and liked. this is for law enforcement and we have attached a previous business card as an example. This site forces me to select color and font, ignore those as I picked stuff just to get this completed.

Target Market(s)

law enforcement, local government

Contact Information for Business Card

see the attached example and our website

Font styles to use
Serif

```html
<!DOCTYPE html>
<html lang="en">
<head>
<meta charset="utf-8">
<title>Dorwial Business Card</title>
<link href="https://fonts.googleapis.com/css2?family=Raleway:wght@300&family=Lato:wght@400;700&display=swap" rel="stylesheet">
<style>
  :root {
    --page: #e6e7e9;
    --navy: #0d2131;
    --navy-glow: #1d4a63;
    --white: #ffffff;
    --ink: #0f1e2b;
    --muted: #5d6670;
    --swoosh: #8d9196;
  }
  * { margin: 0; padding: 0; box-sizing: border-box; }
  html, body { width: 1200px; height: 900px; overflow: hidden; }
  body {
    background: var(--page);
    font-family: "Lato", sans-serif;
    display: flex;
    flex-direction: column;
    align-items: center;
    justify-content: center;
    gap: 40px;
  }
  .card {
    position: relative;
    width: 660px;
    height: 377px;
    overflow: hidden;
    box-shadow: 0 6px 18px rgba(0,0,0,0.18);
  }

  /* Front */
  .card-front { background: var(--navy); color: var(--white); }
  .network-map {
    position: absolute; inset: 0;
    background: radial-gradient(ellipse at 60% 45%, var(--navy-glow) 0%, var(--navy) 70%);
  }
  .front-brand {
    position: absolute; left: 0; right: 0; top: 120px;
    text-align: center;
    font-family: "Raleway", sans-serif;
    font-weight: 300;
    font-size: 58px;
    letter-spacing: 10px;
  }
  .front-tagline {
    position: absolute; left: 0; right: 0; top: 232px;
    text-align: center;
    font-size: 15px;
    letter-spacing: 1.5px;
  }

  /* Back */
  .card-back { background: var(--white); color: var(--ink); }
  .back-wave { position: absolute; inset: 0; }
  .back-brand {
    position: absolute; right: 34px; top: 48px;
    font-family: "Raleway", sans-serif;
    font-weight: 300;
    font-size: 50px;
    letter-spacing: 7px;
    color: var(--ink);
  }
  .holder { position: absolute; left: 52px; top: 72px; }
  .holder-name { font-weight: 700; font-size: 20px; letter-spacing: 0.5px; }
  .holder-title { font-size: 15px; color: var(--muted); margin-top: 1px; }
  .contact-list {
    position: absolute; left: 52px; top: 150px;
    list-style: none;
    font-size: 16px; color: var(--muted);
  }
  .contact-list li { display: flex; align-items: center; gap: 7px; line-height: 22px; }
  .contact-list svg { width: 13px; height: 13px; fill: var(--ink); }
  .address {
    position: absolute; left: 70px; top: 222px;
    font-size: 17px; color: var(--muted); line-height: 22px;
  }
  .service-line {
    position: absolute; right: 30px; bottom: 26px;
    font-size: 15px; color: var(--white); letter-spacing: 0.3px;
  }
</style>
</head>
<body>

<section class="card card-front">
  <div class="network-map" role="img" aria-label="Faint network of connected points over a map of the United States"></div>
  <div class="front-brand">DORWIAL</div>
  <div class="front-tagline">LAW ENFORCEMENT INNOVATION</div>
</section>

<section class="card card-back">
  <svg class="back-wave" viewBox="0 0 660 377" preserveAspectRatio="none" aria-hidden="true">
    <path fill="var(--swoosh)" d="M0,278 C160,318 300,288 420,215 C505,166 585,158 660,160 L660,172 C590,170 520,178 430,230 C310,300 160,326 0,300 Z"/>
    <path fill="var(--navy)" d="M0,300 C160,326 310,300 430,230 C520,178 590,170 660,172 L660,377 L0,377 Z"/>
  </svg>

  <div class="back-brand">DORWIAL</div>

  <div class="holder">
    <div class="holder-name">MARCUS ELLERY</div>
    <div class="holder-title">Managing Director</div>
  </div>

  <ul class="contact-list">
    <li>
      <svg viewBox="0 0 16 16"><path d="M3 1h3l1.5 3.5-2 1.3a9 9 0 0 0 4.7 4.7l1.3-2L15 10v3a2 2 0 0 1-2 2A12 12 0 0 1 1 3a2 2 0 0 1 2-2z"/></svg>
      866.555.0142
    </li>
    <li>
      <svg viewBox="0 0 16 16"><path d="M1 3h14v10H1z M1 3l7 6 7-6" fill="none" stroke="var(--ink)" stroke-width="1.6"/></svg>
      info@dorwian.com
    </li>
    <li>
      <svg viewBox="0 0 16 16"><circle cx="8" cy="8" r="7"/><path d="M1 8h14M8 1c3 3 3 11 0 14M8 1c-3 3-3 11 0 14" fill="none" stroke="var(--white)" stroke-width="1"/></svg>
      www.dorwian.com
    </li>
  </ul>

  <address class="address" style="font-style: normal;">
    2140 Larkspur Drive<br>Houston, TX 77042
  </address>

  <div class="service-line">Law Enforcement &#9679; Justice of the Peace &#9679; Municipal Courts</div>
</section>

</body>
</html>
```